Business Card Design Project

"Crest Ledger Systems" is database management company working in the direct marketing & digital printing industries. Currently going through a name & rebranding process we require a new company business card.

Industry/Entity Type

Marketing

```html
<!DOCTYPE html>
<html lang="en">
<head>
<meta charset="utf-8">
<title>Crest Ledger Systems – Business Card</title>
<link href="https://fonts.googleapis.com/css2?family=Mulish:wght@400;700&display=swap" rel="stylesheet">
<style>
  :root {
    --page-bg: #e4e4e6;
    --card-light: #fbfbfb;
    --card-mid: #e2e2e3;
    --brand-blue: #129fd8;
    --brand-blue-dark: #0b87bd;
    --slate: #474d57;
    --slate-dark: #3c414a;
    --ink: #2f3640;
    --ink-soft: #3a4450;
    --contact-text: #e9ecef;
    --icon: #1c8fc5;
  }
  * { box-sizing: border-box; margin: 0; padding: 0; }
  html, body {
    width: 1200px; height: 900px; overflow: hidden;
    background: var(--page-bg);
    font-family: "Mulish", "Century Gothic", sans-serif;
  }
  .sheet {
    position: relative; width: 1200px; height: 900px;
    display: flex; flex-direction: column; align-items: center; justify-content: center; gap: 44px;
  }
  .card {
    position: relative; width: 680px; height: 388px;
    border-radius: 22px; overflow: hidden;
    background: linear-gradient(160deg, var(--card-light) 0%, #f1f1f2 45%, var(--card-mid) 100%);
    box-shadow: 0 10px 26px rgba(0,0,0,.22);
  }
  .wordmark {
    display: flex; align-items: center; gap: 10px;
    font-weight: 700; color: var(--ink); letter-spacing: -0.5px;
  }
  .wordmark__mark { width: 22px; height: 22px; background: var(--brand-blue); border-radius: 3px; }
  .card--front { display: flex; align-items: center; justify-content: center; }
  .card--front .wordmark { font-size: 40px; }
  .card--front .wordmark__mark { width: 30px; height: 30px; }

  .card--back .wordmark { position: absolute; left: 44px; top: 60px; font-size: 29px; }
  .band-name {
    position: absolute; left: 0; top: 140px; width: 300px; height: 148px;
    background: linear-gradient(180deg, var(--brand-blue) 0%, var(--brand-blue-dark) 100%);
    padding: 48px 0 0 44px;
  }
  .band-name__person { font-size: 21px; font-weight: 700; color: var(--ink); }
  .band-name__role { margin-top: 8px; font-size: 15px; color: var(--ink-soft); }
  .band-contact {
    position: absolute; left: 300px; top: 104px; right: 0; height: 118px;
    background: linear-gradient(180deg, var(--slate) 0%, var(--slate-dark) 100%);
    padding: 16px 0 0 132px;
  }
  .contact-list { list-style: none; }
  .contact-list li {
    display: flex; align-items: center; gap: 14px;
    font-size: 15px; color: var(--contact-text); line-height: 26px;
  }
  .contact-list svg { width: 13px; height: 13px; flex: none; }
</style>
</head>
<body>
<main class="sheet">
  <section class="card card--front" aria-label="Card front">
    <div class="wordmark"><span class="wordmark__mark"></span>Crest Ledger Systems</div>
  </section>

  <section class="card card--back" aria-label="Card back">
    <div class="wordmark"><span class="wordmark__mark"></span>Crest Ledger Systems</div>
    <div class="band-contact">
      <ul class="contact-list">
        <li>
          <svg viewBox="0 0 16 16" aria-hidden="true"><path fill="var(--icon)" d="M3.5 1l3 3-1.6 1.8a9 9 0 0 0 5.3 5.3L12 9.5l3 3-2 2.3C6.5 14.5 1.5 9.5 1.2 3z"/></svg>
          +61 987 210
        </li>
        <li>
          <svg viewBox="0 0 16 16" aria-hidden="true"><circle cx="8" cy="8" r="6.5" fill="none" stroke="var(--icon)" stroke-width="2"/><circle cx="8" cy="8" r="2.5" fill="var(--icon)"/></svg>
          harlow@crestledger.com
        </li>
        <li>
          <svg viewBox="0 0 16 16" aria-hidden="true"><circle cx="8" cy="8" r="6.5" fill="none" stroke="var(--icon)" stroke-width="1.6"/><path d="M1.5 8h13M8 1.5c3 3 3 10 0 13M8 1.5c-3 3-3 10 0 13" fill="none" stroke="var(--icon)" stroke-width="1.4"/></svg>
          www.crestledger.com
        </li>
      </ul>
    </div>
    <div class="band-name">
      <p class="band-name__person">Owen Harlow</p>
      <p class="band-name__role">General meneger</p>
    </div>
  </section>
</main>
</body>
</html>
```